My name is Tomas Verenda, and I have done business with your company several times. I need a business card to represent my business, I own a company by the name of BELOMI Suntan Lotion & Sunscreen.
My requirements are as follow: My company logo in the brightest gold possible, on a black, grainy (sandy) background, with shading around the each element. With the company name in gold, a stylized coconut trees, and some type of wave graphic in gold. "A product of the USA, Marlow Bay, ME"
"For comments, suggestion, or ordering please contact us at:
belomi42@nexamail.test"

"BELOMI™ Tanning Lotion & Sunscreen―Crafted with Care"

Belomi Tanning Lotion & Sunscreen is the most extraordinary and innovative sun tanning product to emerge in several generations. The constituents of this product are formidable substances that protect the skin against the aftermath of sun exposure−before you exposed yourself to the sun’s rays. The Aloe Vera in this product, along with other oils and cream, are specifically manufactured to lessen the symptoms of extended exposure to the sun. Belomi is designed to provide a Broad Spectrum Protection (50) that assist in the reduction of (UVA) and (UVB) radiation to create a magnificent sun-absorbing, long-lasting, deep dark bronzing experience.
Thank you,
Tomas Verenda
tomastverenda@postline.test

Target Market(s)

Sunscreen

Industry/Entity Type

Business

Contact Information for Business Card

BELOMI™ Tanning Lotion and Sunscreen
Crafted with Care

Belomi Tanning Lotion is the most extraordinary and innovative sun tanning product to emerge in several generations. The constituents of this product are formidable substances that protect the skin against the aftermath of sun exposure−before you exposed yourself to the sun’s rays. The Aloe Vera, in this product, along with other oils and cream, are specifically manufactured to lessen the symptoms of extended exposure to the sun. Belomi protects your skin from dehydration and treat your skin with the products we apply to ourselves after a sunburn−before the sun tanning process begins. Belomi is designed to provide a Broad Spectrum Protection (50) that assist in the reduction of (UVA) and (UVB) radiation to create a magnificent sun-absorbing, long-lasting, deep dark bronzing experience.

Colors
fece3e
acd136

Requirements
Must have
• Black Card Stock with grainy surface, Gold Logo, stylized Coconut Palm Tree, Company Name, email address, and NYC location.
• Modern Layout with Modern fonts and graphics

```html
<!DOCTYPE html>
<html lang="en">
<head>
<meta charset="utf-8">
<title>BELOMI Suntan Lotion – Business Card</title>
<link rel="stylesheet" href="https://fonts.googleapis.com/css2?family=Open+Sans:wght@400;600;700&display=swap">
<style>
  :root {
    --stage: #8f8f8f;
    --card: #151515;
    --gold: #fece3e;
    --gold-deep: #c99a52;
    --gold-dark: #7a4a1c;
    --tan: #c9a06b;
    --name-gold: #d3a45e;
    --title-gold: #e9bf3c;
    --text-soft: #cfcfcf;
    --text-white: #ffffff;
    --divider: #4a4a4a;
  }
  * { box-sizing: border-box; margin: 0; padding: 0; }
  html, body {
    width: 1105px; height: 1200px; overflow: hidden;
    background: var(--stage);
    font-family: "Open Sans", Arial, sans-serif;
  }
  .canvas { position: relative; width: 1105px; height: 1200px; }
  .card {
    position: absolute; left: 196px; width: 720px; height: 413px;
    background-color: var(--card);
    background-image:
      radial-gradient(rgba(255,255,255,0.06) 0.6px, transparent 1px),
      radial-gradient(rgba(0,0,0,0.35) 0.6px, transparent 1px);
    background-size: 3px 3px, 4px 4px;
    background-position: 0 0, 1px 2px;
    box-shadow: 0 4px 10px rgba(0,0,0,0.45);
    overflow: hidden;
  }
  .card--front { top: 145px; }
  .card--back { top: 602px; }

  /* front: brand block */
  .brand-mark {
    position: absolute; left: 163px; top: 121px; width: 100px; height: 100px;
    border-radius: 50%;
    background: radial-gradient(circle at 40% 35%, var(--gold), var(--gold-deep) 70%, var(--gold-dark));
  }
  .brand-name {
    position: absolute; left: 0; width: 428px; top: 227px;
    text-align: center; color: var(--name-gold);
    font-weight: 600; font-size: 42px; letter-spacing: 2px; line-height: 1;
  }
  .brand-tagline {
    position: absolute; left: 0; width: 428px; top: 274px;
    text-align: center; color: var(--name-gold);
    font-size: 17px; letter-spacing: 0.5px; line-height: 1;
  }
  .divider {
    position: absolute; left: 374px; top: 117px; width: 1px; height: 177px;
    background: var(--divider);
  }

  /* front: contact block */
  .contact { position: absolute; left: 421px; top: 125px; }
  .contact-name {
    color: var(--name-gold); font-weight: 700; font-size: 26px;
    letter-spacing: 0.5px; line-height: 1.1;
  }
  .contact-role {
    color: var(--title-gold); font-weight: 600; font-size: 19px;
    margin-top: 2px; line-height: 1.2;
  }
  .contact-list { list-style: none; margin-top: 16px; }
  .contact-item {
    display: flex; align-items: center; gap: 10px;
    color: var(--text-soft); font-size: 18px; line-height: 27.5px;
  }
  .contact-item svg { width: 17px; height: 17px; fill: var(--text-soft); flex: none; }

  /* front: bottom band */
  .band { position: absolute; left: 0; bottom: 0; width: 720px; height: 29px; }

  /* back */
  .back-mark {
    position: absolute; left: 244px; top: 54px; width: 216px; height: 216px;
    border-radius: 50%;
    border: 4px solid var(--gold);
    display: flex; align-items: center; justify-content: center;
  }
  .back-mark-name {
    color: var(--gold); font-weight: 600; font-size: 40px; letter-spacing: 2px;
  }
  .back-info {
    position: absolute; left: 0; width: 720px; top: 293px;
    text-align: center; color: var(--text-white);
    font-size: 18px; line-height: 25.5px;
  }
  .back-email { font-weight: 700; font-size: 20px; margin-top: 1px; }
</style>
</head>
<body>
<main class="canvas">

  <section class="card card--front" aria-label="Business card front">
    <div class="brand-mark" aria-hidden="true"></div>
    <div class="brand-name">BELOMI</div>
    <div class="brand-tagline">SUNTAN LOTION</div>

    <div class="divider"></div>

    <div class="contact">
      <div class="contact-name">TOMAS VERENDA</div>
      <div class="contact-role">CEO/Founder</div>
      <ul class="contact-list">
        <li class="contact-item">
          <svg viewBox="0 0 24 24" aria-hidden="true"><path d="M6.6 10.8a15.1 15.1 0 0 0 6.6 6.6l2.2-2.2c.3-.3.7-.4 1-.2 1.1.4 2.3.6 3.6.6.6 0 1 .4 1 1V20c0 .6-.4 1-1 1A17 17 0 0 1 3 4c0-.6.4-1 1-1h3.5c.6 0 1 .4 1 1 0 1.3.2 2.5.6 3.6.1.3 0 .7-.2 1z"/></svg>
          555 014 7261
        </li>
        <li class="contact-item">
          <svg viewBox="0 0 24 24" aria-hidden="true"><path d="M7 1h10a2 2 0 0 1 2 2v18a2 2 0 0 1-2 2H7a2 2 0 0 1-2-2V3a2 2 0 0 1 2-2zm0 3v14h10V4zm5 15.5a1.2 1.2 0 1 0 0 2.4 1.2 1.2 0 0 0 0-2.4z"/></svg>
          555 019 3408
        </li>
        <li class="contact-item">
          <svg viewBox="0 0 24 24" aria-hidden="true"><path d="M12 2a10 10 0 1 0 0 20 10 10 0 0 0 0-20zm-1 17.9A8 8 0 0 1 4.2 10.2L9 15v1a2 2 0 0 0 2 2zm6.9-2.5A2 2 0 0 0 16 16h-1v-3a1 1 0 0 0-1-1H8v-2h2a1 1 0 0 0 1-1V7h2a2 2 0 0 0 2-2v-.4a8 8 0 0 1 2.9 12.8z"/></svg>
          www.belomi.test
        </li>
      </ul>
    </div>

    <svg class="band" viewBox="0 0 720 29" preserveAspectRatio="none" aria-hidden="true">
      <defs>
        <linearGradient id="band-gold" x1="0" x2="1" y1="0" y2="0">
          <stop offset="0" stop-color="#7a4a1c"/>
          <stop offset="0.25" stop-color="#b9873a"/>
          <stop offset="0.5" stop-color="#f3dc74"/>
          <stop offset="0.75" stop-color="#b98336"/>
          <stop offset="1" stop-color="#6e3f18"/>
        </linearGradient>
      </defs>
      <polygon points="0,0 468,0 460,29 0,29" fill="url(#band-gold)"/>
      <polygon points="476,0 720,0 720,29 468,29" fill="var(--tan)"/>
    </svg>
  </section>

  <section class="card card--back" aria-label="Business card back">
    <div class="back-mark">
      <span class="back-mark-name">BELOMI</span>
    </div>
    <div class="back-info">
      <p>A product of the USA, Marlow Bay, ME</p>
      <p>For comments, suggestion, or ordering please contact us at:</p>
      <p class="back-email">belomi42@nexamail.test</p>
    </div>
  </section>

</main>
</body>
</html>
```